Design Home Screen

We’re looking for talented UI/UX designers to create an eye-popping, modern, and fun Home Screen for the Plenk app — the future of real-time earned wage access and financial empowerment.
Your mission: make the Plenk experience come alive the moment users open the app.

Design Goals

The screen should instantly communicate energy, financial control, and trust.

The “Time on the Clock” and the “Plenk Balance” must be the stars of the screen — presented in a way that feels alive, interactive, and rewarding.

Think of how to visually celebrate a user’s progress at work and their earnings — something that makes checking the app feel fun and satisfying, not transactional.

Creative Direction

Style: Sleek, fintech-modern, with motion or visual elements that feel alive (micro-animations, glowing accents, gradient depth, or movement cues).

Tone: Confident, vibrant, and optimistic — this is a financial app that feels human and inspiring.

Color palette: Black, Gold, and Green, and any other color.

Typography: Clean, readable, and balanced between playful and professional.

Must-Have Elements

Time on the Clock – creatively displayed (e.g., countdown or progress animation as the user works).

Plenk Balance – bold, fun, and maybe even interactive (reflecting growth as the user earns).

A clean navigation structure for core tabs: Home, Access Pay, Boost, History, Profile.

Engaging micro-animations, icons, or progress indicators that make the user feel “in motion.”

Room for brand personality — the “Plenk” name and logo if desired.

```html
<!DOCTYPE html>
<html lang="en">
<head>
<meta charset="utf-8">
<title>Plenk — Home</title>
<link href="https://fonts.googleapis.com/css2?family=Poppins:wght@400;500;600;700&display=swap" rel="stylesheet">
<style>
:root{
  --bg:#000;
  --card:#1e1f1d;
  --nav:#1b1b1b;
  --gold:#e8b94a;
  --gold-dark:#a8852e;
  --green:#3fae7c;
  --ring-track:#2d3a2c;
  --white:#fff;
  --muted:#8a8a8a;
  --red:#e0393e;
}
*{margin:0;padding:0;box-sizing:border-box}
html,body{width:1200px;height:4080px;overflow:hidden;background:var(--bg)}
body{font-family:'Poppins',sans-serif;color:var(--white);position:relative}
.abs{position:absolute}
.status-time{left:86px;top:48px;font-size:46px;font-weight:600}
.status-icons{right:48px;top:54px}
.avatar{left:64px;top:173px;width:160px;height:160px;border-radius:50%;background:radial-gradient(circle at 50% 40%,#6b5a4e,#2c2420 70%)}
.welcome{left:277px;top:186px;font-size:36px;color:#9a9a9a}
.user-name{left:277px;top:250px;font-size:58px;font-weight:500}
.bell{left:1002px;top:186px;width:134px;height:134px;border-radius:50%;background:linear-gradient(160deg,#e2b84b,#8f6d22);display:flex;align-items:center;justify-content:center}
.clock-title{left:0;width:1200px;top:446px;text-align:center;font-size:40px;font-weight:500}
.clock{left:150px;top:499px}
.clock-time{left:0;width:1200px;top:870px;text-align:center;font-size:134px;font-weight:700;letter-spacing:4px;line-height:1}
.clock-time small{font-size:38px;letter-spacing:4px;margin-left:10px}
.hours-row{left:67px;right:64px;top:1460px;display:flex;align-items:center;font-size:42px}
.hours-row .label{flex:1;font-weight:500}
.hours-row .hrs{color:var(--gold);font-weight:500}
.hours-row .sep{width:3px;height:76px;background:#555;transform:rotate(14deg);margin:0 22px}
.hours-row .rate{color:var(--green);font-weight:500;font-size:46px}
.balance-card{left:67px;top:1592px;width:1069px;height:504px;border-radius:32px;background:var(--card)}
.balance-label{top:68px;width:100%;text-align:center;font-size:42px;font-weight:500}
.balance-amount{top:130px;width:100%;text-align:center;font-size:166px;font-weight:700;color:var(--gold);line-height:1.2}
.period{left:64px;right:67px;top:378px;display:flex;align-items:baseline;font-size:42px}
.period .label{flex:1;font-weight:500}
.period .month{color:var(--gold);font-size:38px;margin-right:20px}
.period .date{color:var(--gold);font-size:48px}
.actions{left:0;top:2176px;width:1200px;height:300px}
.action{position:absolute;width:300px;margin-left:-150px;text-align:center}
.action .btn{width:172px;height:172px;margin:0 auto;border-radius:50%;background:linear-gradient(160deg,#e2b84b,#8f6d22);display:flex;align-items:center;justify-content:center}
.action .lbl{margin-top:20px;font-size:42px;line-height:48px}
.divider{left:70px;right:64px;top:2555px;height:2px;background:#1f1f1f}
.tx-title{left:64px;top:2640px;font-size:58px;font-weight:500}
.see-all{right:64px;top:2655px;font-size:45px;font-weight:500;color:var(--gold)}
.tx{left:0;width:1200px;height:150px}
.tx .logo{position:absolute;left:64px;top:8px;width:134px;height:134px;border-radius:50%}
.tx .name{position:absolute;left:253px;top:2px;font-size:52px;font-weight:500}
.tx .date{position:absolute;left:253px;top:78px;font-size:38px;color:var(--muted)}
.tx .amount{position:absolute;right:317px;top:38px;font-size:52px;font-weight:500}
.tx .state{position:absolute;right:64px;top:34px;font-size:39px;font-weight:500;text-align:right;line-height:40px}
.tx .state span{display:block;color:var(--white);font-size:35px;font-weight:400}
.sent{color:var(--green)}.pending{color:var(--gold)}.failed{color:var(--red)}
.nav{left:0;top:3805px;width:1200px;height:275px;background:var(--nav);border-radius:0 0 48px 48px}
.nav-item{position:absolute;top:60px;width:240px;margin-left:-120px;text-align:center;font-size:35px;color:#8c8c8c}
.nav-item svg{display:block;margin:0 auto 10px}
.nav-item.active{color:var(--gold)}
</style>
</head>
<body>
<div class="abs status-time">9:41</div>
<svg class="abs status-icons" width="112" height="40" viewBox="0 0 112 40">
  <g fill="#fff"><rect x="0" y="24" width="7" height="10" rx="2"/><rect x="11" y="18" width="7" height="16" rx="2"/><rect x="22" y="12" width="7" height="22" rx="2"/><rect x="33" y="5" width="7" height="29" rx="2"/></g>
</svg>
<svg class="abs" style="left:1024px;top:52px" width="130" height="40" viewBox="0 0 130 40">
  <path d="M4 14a26 26 0 0 1 36 0M10 21a17 17 0 0 1 24 0M17 28a7 7 0 0 1 10 0" stroke="#fff" stroke-width="5" fill="none" stroke-linecap="round"/>
  <rect x="52" y="4" width="70" height="32" rx="9" stroke="#fff" stroke-width="3" fill="none"/>
  <rect x="57" y="9" width="60" height="22" rx="5" fill="#fff"/>
</svg>

<div class="abs avatar" role="img" aria-label="Profile photo of the user"></div>
<div class="abs welcome">Welcome back,</div>
<div class="abs user-name">Mara Okafor</div>
<div class="abs bell">
  <svg width="62" height="62" viewBox="0 0 24 24" fill="none" stroke="#fff" stroke-width="1.6" stroke-linecap="round" stroke-linejoin="round"><path d="M6 16V11a6 6 0 0 1 12 0v5l1.5 2h-15z"/><path d="M10 20a2 2 0 0 0 4 0"/></svg>
</div>

<div class="abs clock-title">Status On the Clock</div>
<svg class="abs clock" width="900" height="900" viewBox="-450 -450 900 900">
  <defs>
    <linearGradient id="arc" x1="0" y1="-1" x2="0" y2="1" gradientUnits="objectBoundingBox">
      <stop offset="0" stop-color="#b08a35"/><stop offset="1" stop-color="#f0c24e"/>
    </linearGradient>
  </defs>
  <circle r="385" fill="none" stroke="#c99a35" stroke-width="14" stroke-dasharray="2 18.16" opacity=".8"/>
  <g stroke="#e0b143" stroke-width="4" stroke-linecap="round">
    <line y1="-378" y2="-406" transform="rotate(0)"/><line y1="-378" y2="-406" transform="rotate(30)"/>
    <line y1="-378" y2="-406" transform="rotate(60)"/><line y1="-378" y2="-406" transform="rotate(90)"/>
    <line y1="-378" y2="-406" transform="rotate(120)"/><line y1="-378" y2="-406" transform="rotate(150)"/>
    <line y1="-378" y2="-406" transform="rotate(180)"/><line y1="-378" y2="-406" transform="rotate(210)"/>
    <line y1="-378" y2="-406" transform="rotate(240)"/><line y1="-378" y2="-406" transform="rotate(270)"/>
    <line y1="-378" y2="-406" transform="rotate(300)"/><line y1="-378" y2="-406" transform="rotate(330)"/>
  </g>
  <circle r="323" fill="none" stroke="var(--ring-track)" stroke-width="58"/>
  <path d="M0 -323 A323 323 0 0 1 0 323" fill="none" stroke="url(#arc)" stroke-width="58" stroke-linecap="round"/>
</svg>
<div class="abs clock-time">10:09<small>AM</small></div>

<div class="abs hours-row">
  <span class="label">Work Hours:</span>
  <span class="hrs">15:00 HRS.</span><span class="sep"></span><span class="rate">@$20.00/hr</span>
</div>

<div class="abs balance-card">
  <div class="abs balance-label">Plenk Wage Balance:</div>
  <div class="abs balance-amount">$12,450</div>
  <div class="abs period"><span class="label">Current Pay Period:</span><span class="month">JUNE</span><span class="date">01/06/2025</span></div>
</div>

<div class="abs actions">
  <div class="action" style="left:154px"><div class="btn"><svg width="64" height="64" viewBox="0 0 24 24" fill="none" stroke="#fff" stroke-width="1.5" stroke-linecap="round" stroke-linejoin="round"><path d="M12 4v11M8 11l4 4 4-4M5 17a7 4 0 0 0 14 0"/></svg></div><div class="lbl">Request<br>Money</div></div>
  <div class="action" style="left:451px"><div class="btn"><svg width="70" height="70" viewBox="0 0 24 24" fill="none" stroke="#fff" stroke-width="1.5" stroke-linecap="round" stroke-linejoin="round"><path d="M19 10a8 8 0 1 1-5-6"/><path d="M20 3l-4 4M16 4v3h3"/><path d="M14 9.5c-.5-1-3.5-1.2-3.5.5s3.8 1 3.6 3c-.2 1.6-3 1.4-3.7.4M12.2 7.5v9"/></svg></div><div class="lbl">Loan<br>Access</div></div>
  <div class="action" style="left:749px"><div class="btn"><svg width="70" height="70" viewBox="0 0 24 24" fill="none" stroke="#fff" stroke-width="1.5" stroke-linecap="round"><circle cx="12" cy="12" r="8"/><path d="M12 8v8M8 12h8"/></svg></div><div class="lbl">Update<br>Employment</div></div>
  <div class="action" style="left:1050px"><div class="btn"><svg width="70" height="70" viewBox="0 0 24 24" fill="none" stroke="#fff" stroke-width="1.5" stroke-linejoin="round"><path d="M5 7h12a2 2 0 0 1 2 2v8a2 2 0 0 1-2 2H6a2 2 0 0 1-2-2V7l10-2v2"/><circle cx="16" cy="13" r="1.2"/></svg></div><div class="lbl">Earn<br>$10,000</div></div>
</div>

<div class="abs divider"></div>
<div class="abs tx-title">Transaction</div>
<div class="abs see-all">See All</div>

<div class="abs tx" style="top:2770px">
  <div class="logo" role="img" aria-label="Portrait photo of the payer" style="background:radial-gradient(circle,#c9c3bb,#7d776f)"></div>
  <div class="name">Jordan Vale Inc.</div><div class="date">Sep 10, 2025</div>
  <div class="amount">$5,99</div><div class="state sent">Sent<span>Paywell</span></div>
</div>
<div class="abs tx" style="top:2975px">
  <div class="logo" style="background:#1a1a1a"></div>
  <div class="name">Corvane Inc.</div><div class="date">June 19, 2025</div>
  <div class="amount">$12,99</div><div class="state sent">Sent<span>Paywell</span></div>
</div>
<div class="abs tx" style="top:3179px">
  <div class="logo" style="background:#14a800"></div>
  <div class="name">Taskloom</div><div class="date">Sep 10, 2025</div>
  <div class="amount">$300</div><div class="state pending">Pending<span>Paywell</span></div>
</div>
<div class="abs tx" style="top:3384px">
  <div class="logo" style="background:#fff"></div>
  <div class="name">Petalwise Deals</div><div class="date">June 19, 2025</div>
  <div class="amount">$88</div><div class="state sent">Sent<span>Paywell</span></div>
</div>
<div class="abs tx" style="top:3589px">
  <div class="logo" style="background:#f2375a"></div>
  <div class="name">Roomnest</div><div class="date">Sep 10, 2025</div>
  <div class="amount">$5,99</div><div class="state failed">Failed<span>Paywell</span></div>
</div>

<nav class="abs nav">
  <div class="nav-item active" style="left:120px"><svg width="70" height="70" viewBox="0 0 24 24" fill="none" stroke="currentColor" stroke-width="1.5" stroke-linejoin="round"><path d="M4 10l8-6 8 6v8a2 2 0 0 1-2 2H6a2 2 0 0 1-2-2z"/><path d="M9 15h6" stroke-linecap="round"/></svg>Home</div>
  <div class="nav-item" style="left:360px"><svg width="70" height="70" viewBox="0 0 24 24" fill="none" stroke="currentColor" stroke-width="1.5"><rect x="3" y="5" width="18" height="14" rx="2"/><path d="M3 10h18M7 15h2M11 15h3"/></svg>Access Pay</div>
  <div class="nav-item" style="left:600px"><svg width="70" height="70" viewBox="0 0 24 24" fill="none" stroke="currentColor" stroke-width="1.5" stroke-linecap="round"><path d="M7 17L17 7M10 7h7v7M7 12l5-5M7 20l3-3"/></svg>Boost</div>
  <div class="nav-item" style="left:840px"><svg width="70" height="70" viewBox="0 0 24 24" fill="none" stroke="currentColor" stroke-width="1.5" stroke-linecap="round"><path d="M4 12a8 8 0 1 0 2.3-5.6M4 4v3h3"/><path d="M12 8v4l3 2"/></svg>History</div>
  <div class="nav-item" style="left:1080px"><svg width="70" height="70" viewBox="0 0 24 24" fill="none" stroke="currentColor" stroke-width="1.5"><circle cx="12" cy="8" r="4"/><path d="M4 21a8 8 0 0 1 16 0"/></svg>Profile</div>
</nav>
</body>
</html>
```